Business Card Design Project

We discover connections between taxi drivers and passengers, improve service quality and save time for both parties.
We need a business card design for a mobile applications company in Melbourne called Hop Along Rides.
Our initial application - HopAlongRides - has taxi and passenger parts, and as such there has to be some sort of link between cab colors (gold/yellow and black) and passengers. Passenger color can be chosen at will and be in harmony with cab colors. Card should also include a symbol of mobile technology such as mobile phone, wireless signal or something else that people associate with mobile applications. Final design should communicate connection between taxis and passengers that is created or refers to mobile phone or tablet (mobile technologies).
Keep in mind that we need a logo as part of the design.
Winning design will be favoured for our next designs that will be posted here!

Target Market(s)

taxi drivers, businessmen/businesswomen, entrepreneurs, contractors, ceos, executives

Industry/Entity Type

Taxi

Requirements
Must have
• This is a product business card, not a personal business card. Therefore it has to include product logo, a slogan under product name and links to social networks - Updates, Social, contact e-mail address and website link with corresponding icons.
Reference to taxi/cab and passenger businesslike figure with variations of male and female.
Reference to mobile technologies such as phone, tablet or mobile connectivity.
Card must be designed and have an exact fit for 1039 x 697 pixels (300dpi)

```html
<!DOCTYPE html>
<html lang="fr">
<head>
<meta charset="utf-8">
<title>Hop Along Rides – Business Card</title>
<link href="https://fonts.googleapis.com/css2?family=Roboto:wght@400;500;700;900&display=swap" rel="stylesheet">
<style>
:root{
  --stage:#2c2d30;
  --stage-light:#4a4b4f;
  --screen-dark:#2a2a2b;
  --screen-mid:#3b3b3d;
  --icon-light:#e4e4e4;
  --icon-dark:#8e8e92;
  --cab-yellow:#f1e31a;
  --ink:#141414;
  --white:#ffffff;
  --label-blue:#5a6f95;
  --nav-top:#b9bfc9;
  --nav-bottom:#7d8797;
  --info-bg:#a9acb2;
  --tab-bg:#1c1c1d;
}
*{box-sizing:border-box;margin:0;padding:0}
html,body{width:1200px;height:800px;overflow:hidden}
body{
  background:radial-gradient(ellipse at 50% 30%,var(--stage-light),var(--stage) 70%);
  font-family:"Roboto",Helvetica,Arial,sans-serif;
  position:relative;
}
.card{
  position:absolute;top:87px;width:420px;height:626px;
  border-radius:6px;overflow:hidden;
  box-shadow:0 18px 40px rgba(0,0,0,.55);
}
.card--front{left:150px;background:linear-gradient(180deg,var(--screen-mid),var(--screen-dark))}
.card--back{left:630px;background:var(--info-bg)}

.status-bar{
  height:22px;display:flex;align-items:center;justify-content:space-between;
  padding:0 8px;font-size:12px;font-weight:700;color:var(--white);
  background:linear-gradient(#3d3d3f,#1d1d1e);
}
.status-bar .carrier{display:flex;align-items:center;gap:5px}
.status-bar .carrier b{color:#7fb2ff;font-weight:700}
.status-bar .battery{width:24px;height:11px;border:1.5px solid var(--white);border-radius:2px;position:relative}
.status-bar .battery::after{content:"";position:absolute;inset:1px;background:var(--white)}

/* Home screen */
.app-grid{
  display:grid;grid-template-columns:repeat(4,1fr);
  row-gap:18px;padding:18px 14px 0;
}
.app{display:flex;flex-direction:column;align-items:center;gap:5px}
.app-icon{
  width:66px;height:66px;border-radius:14px;
  background:linear-gradient(180deg,var(--icon-light),var(--icon-dark));
  box-shadow:0 2px 4px rgba(0,0,0,.6);
  display:flex;align-items:center;justify-content:center;position:relative;overflow:hidden;
}
.app-icon::before{content:"";position:absolute;left:0;right:0;top:0;height:50%;background:rgba(255,255,255,.25);border-radius:0 0 50% 50%/0 0 20% 20%}
.app-icon--dark{background:linear-gradient(180deg,#7a7a7e,#262628)}
.app-icon--cab{background:var(--cab-yellow)}
.app-icon--cab::before{display:none}
.app-icon svg{position:relative}
.app-label{font-size:12px;color:var(--white);text-shadow:0 1px 2px #000;white-space:nowrap}
.calendar-day{position:relative;font-size:34px;font-weight:700;color:var(--ink);margin-top:10px}
.calendar-month{position:absolute;top:3px;left:0;right:0;text-align:center;font-size:9px;color:var(--white);background:#444;padding:1px 0;z-index:1}

.page-dots{display:flex;justify-content:center;gap:8px;margin-top:26px}
.page-dots span{width:7px;height:7px;border-radius:50%;background:#777}
.page-dots span.is-current{background:var(--white)}

.unlock{
  position:absolute;left:0;right:0;bottom:0;height:96px;
  background:linear-gradient(#1f1f20,#0f0f10);
  padding:20px 18px;
}
.unlock-track{
  height:56px;border-radius:12px;background:linear-gradient(#2b2b2c,#3a3a3c);
  border:1px solid #4a4a4c;display:flex;align-items:center;padding:0 6px;gap:12px;
}
.unlock-knob{
  flex:none;width:76px;height:44px;border-radius:9px;
  background:linear-gradient(#f2f2f2,#a9a9ab);
  display:flex;align-items:center;justify-content:center;
}
.unlock-dot{flex:none;width:18px;height:18px;border-radius:50%;background:#4fb6e8}
.unlock-text{font-size:19px;color:var(--white);white-space:nowrap}
.unlock-text span{color:#8e8e92}

/* Contact info screen */
.nav-bar{
  height:44px;display:flex;align-items:center;justify-content:space-between;padding:0 6px;
  background:linear-gradient(var(--nav-top),var(--nav-bottom));
  border-bottom:1px solid #555d6a;
}
.nav-title{font-size:19px;font-weight:700;color:var(--white);text-shadow:0 -1px 0 #555}
.nav-button{
  font-size:11px;font-weight:700;color:var(--white);padding:7px 9px;border-radius:5px;
  background:linear-gradient(#8a9bb8,#4d6590);border:1px solid #3e4f6f;
}
.brand{display:flex;flex-direction:column;align-items:center;padding-top:22px}
.brand-mark{width:150px;height:150px;border-radius:50%;background:var(--cab-yellow)}
.brand-name{margin-top:16px;font-size:32px;font-weight:900;color:var(--ink)}
.info-table{
  margin:16px 14px 0;background:var(--white);border-radius:14px;
  border:1px solid #888;overflow:hidden;
}
.info-row{
  display:flex;align-items:center;height:44px;padding:0 12px;
  border-bottom:1px solid #d6d6d6;font-size:15px;
}
.info-row:last-child{border-bottom:0}
.info-row dt{width:86px;text-align:right;color:var(--label-blue);font-weight:500;padding-right:10px}
.info-row dd{color:var(--ink);white-space:nowrap}
.tab-bar{
  position:absolute;left:0;right:0;bottom:0;height:60px;background:var(--tab-bg);
  display:grid;grid-template-columns:repeat(5,1fr);
}
.tab{display:flex;flex-direction:column;align-items:center;justify-content:center;gap:4px;font-size:10px;font-weight:700;color:#999}
.tab.is-active{background:#3a3a3c;color:var(--white)}
</style>
</head>
<body>

<section class="card card--front" aria-label="Recto : écran d'accueil">
  <div class="status-bar">
    <span class="carrier">ZELTA <b>3G</b></span><span>4:20 PM</span><span class="battery"></span>
  </div>
  <div class="app-grid">
    <div class="app"><div class="app-icon"><svg width="38" height="30"><ellipse cx="19" cy="14" rx="17" ry="12" fill="#fff"/></svg></div><span class="app-label">Messages</span></div>
    <div class="app"><div class="app-icon" style="background:#fff"><span class="calendar-month">mardi</span><span class="calendar-day">25</span></div><span class="app-label">Calendrier</span></div>
    <div class="app"><div class="app-icon"><svg width="36" height="36"><circle cx="18" cy="18" r="15" fill="#bbb"/><circle cx="18" cy="18" r="5" fill="#eee"/></svg></div><span class="app-label">Photos</span></div>
    <div class="app"><div class="app-icon app-icon--dark"><svg width="36" height="36"><circle cx="18" cy="18" r="15" fill="#222" stroke="#aaa" stroke-width="3"/><circle cx="18" cy="18" r="6" fill="#555"/></svg></div><span class="app-label">Appareil photo</span></div>

    <div class="app"><div class="app-icon app-icon--dark"><svg width="40" height="30"><rect x="2" y="10" width="36" height="18" fill="#ddd"/><rect x="2" y="3" width="36" height="6" fill="#555"/></svg></div><span class="app-label">Vidéos</span></div>
    <div class="app"><div class="app-icon"><svg width="44" height="32"><rect x="2" y="2" width="40" height="28" rx="4" fill="#555"/><rect x="6" y="6" width="32" height="20" fill="#999"/></svg></div><span class="app-label">Flux</span></div>
    <div class="app"><div class="app-icon app-icon--cab" role="img" aria-label="Hop Along Rides app"></div><span class="app-label">Hop Along Rides</span></div>
    <div class="app"><div class="app-icon"><svg width="40" height="30"><ellipse cx="20" cy="18" rx="16" ry="9" fill="#fff"/></svg></div><span class="app-label">Météo</span></div>

    <div class="app"><div class="app-icon" style="background:linear-gradient(#f4f4f4,#cfcfcf)"><svg width="44" height="40"><g stroke="#aaa"><line x1="4" y1="10" x2="40" y2="10"/><line x1="4" y1="20" x2="40" y2="20"/><line x1="4" y1="30" x2="40" y2="30"/></g></svg></div><span class="app-label">Notes</span></div>
    <div class="app"><div class="app-icon" style="background:linear-gradient(#fafafa,#d4d4d4)"><svg width="40" height="40"><g fill="none" stroke="#333" stroke-width="2"><path d="M4 9l3 3 5-6M4 21l3 3 5-6M4 33l3 3 5-6"/></g><g stroke="#888"><line x1="16" y1="9" x2="38" y2="9"/><line x1="16" y1="21" x2="38" y2="21"/><line x1="16" y1="33" x2="38" y2="33"/></g></svg></div><span class="app-label">Rappels</span></div>
    <div class="app"><div class="app-icon app-icon--dark"><svg width="48" height="48"><circle cx="24" cy="24" r="21" fill="#fff"/><path d="M24 24V10M24 24l9 6" stroke="#111" stroke-width="2.5"/></svg></div><span class="app-label">Horloge</span></div>
    <div class="app"><div class="app-icon"><svg width="44" height="44"><path d="M4 30L40 14" stroke="#fff" stroke-width="5"/><circle cx="30" cy="14" r="6" fill="#666"/></svg></div><span class="app-label">Plans</span></div>

    <div class="app"><div class="app-icon" style="background:linear-gradient(#e9e9e9,#9a9a9a)"><svg width="42" height="36"><rect x="4" y="4" width="34" height="28" fill="#777"/><rect x="8" y="8" width="12" height="10" fill="#ddd"/></svg></div><span class="app-label">Kiosque</span></div>
    <div class="app"><div class="app-icon"><svg width="36" height="40"><path d="M12 32V8l18-4v24" stroke="#fff" stroke-width="4" fill="none"/><circle cx="9" cy="32" r="5" fill="#fff"/><circle cx="27" cy="28" r="5" fill="#fff"/></svg></div><span class="app-label">Musique</span></div>
    <div class="app"><div class="app-icon"><svg width="40" height="40"><rect x="7" y="14" width="26" height="22" rx="3" fill="#fff"/><path d="M14 14v-4a6 6 0 0 1 12 0v4" stroke="#fff" stroke-width="3" fill="none"/></svg></div><span class="app-label">Boutique</span></div>
    <div class="app"><div class="app-icon"><svg width="46" height="46"><circle cx="23" cy="23" r="18" fill="none" stroke="#555" stroke-width="7" stroke-dasharray="5 4"/><circle cx="23" cy="23" r="9" fill="#888"/></svg></div><span class="app-label">Réglages</span></div>
  </div>
  <div class="page-dots"><span></span><span class="is-current"></span><span></span></div>
  <div class="unlock">
    <div class="unlock-track">
      <div class="unlock-knob"><svg width="36" height="20"><path d="M2 10h26M20 3l8 7-8 7" stroke="#555" stroke-width="4" fill="none"/></svg></div>
      <span class="unlock-dot"></span>
      <span class="unlock-text">#hopalongrides <span>to unlock</span></span>
    </div>
  </div>
</section>

<section class="card card--back" aria-label="Verso : fiche contact">
  <div class="status-bar">
    <span class="carrier">ZELTA <b>3G</b></span><span>4:20 PM</span><span class="battery"></span>
  </div>
  <div class="nav-bar">
    <span class="nav-button">All Contacts</span><span class="nav-title">Info</span><span class="nav-button">Edit</span>
  </div>
  <div class="brand">
    <span class="brand-mark"></span>
    <span class="brand-name">HopAlongRides</span>
  </div>
  <dl class="info-table">
    <div class="info-row"><dt>Web</dt><dd>info@hopalongrides.app</dd></div>
    <div class="info-row"><dt>Email</dt><dd>info@hopalongrides.app</dd></div>
    <div class="info-row"><dt>Social</dt><dd>friendsnet.com/hopalongrides</dd></div>
    <div class="info-row"><dt>Updates</dt><dd>#hopalongrides</dd></div>
  </dl>
  <nav class="tab-bar">
    <span class="tab"><svg width="26" height="24"><path d="M13 1l3.6 7.6 8.4 1-6.2 5.8 1.6 8.2L13 19.6 5.6 23.6l1.6-8.2L1 9.6l8.4-1z" fill="#999"/></svg>Favorites</span>
    <span class="tab"><svg width="24" height="24"><circle cx="12" cy="12" r="10" fill="none" stroke="#999" stroke-width="2.5"/><path d="M12 6v6l4 3" stroke="#999" stroke-width="2" fill="none"/></svg>Recents</span>
    <span class="tab is-active"><svg width="24" height="24"><circle cx="12" cy="12" r="10" fill="#f1e31a"/></svg>Taxi</span>
    <span class="tab"><svg width="24" height="24" fill="#999"><rect x="1" y="1" width="6" height="6"/><rect x="9" y="1" width="6" height="6"/><rect x="17" y="1" width="6" height="6"/><rect x="1" y="9" width="6" height="6"/><rect x="9" y="9" width="6" height="6"/><rect x="17" y="9" width="6" height="6"/><rect x="1" y="17" width="6" height="6"/><rect x="9" y="17" width="6" height="6"/><rect x="17" y="17" width="6" height="6"/></svg>Keypad</span>
    <span class="tab"><svg width="30" height="20"><circle cx="7" cy="10" r="5" fill="none" stroke="#999" stroke-width="2.5"/><circle cx="23" cy="10" r="5" fill="none" stroke="#999" stroke-width="2.5"/><line x1="7" y1="15" x2="23" y2="15" stroke="#999" stroke-width="2.5"/></svg>Voicemail</span>
  </nav>
</section>

</body>
</html>
```